Advertising tiles for website

Hi
I have a website at www.tagwhistle.co.nz and there are four spots along the top for advertising tiles (at the moment there are dummy tiles in place).

Each tile is 220 wide and 200 high and I would like 4 tiles created as a starting point for this site.

I can change the tiles on every page so conceivably we could have very targeted advertising leading the visitor to services we want to promote (we can set this extension up as a new design job for you). Eg. domains for sale, Escrow services, featured domains, Turnkey Websites, New Websites etc.

The advertisements that I might like see on the website would be as follows:
Gallery Ink
Sell Your Domain
Domains For Sale
Featured Domains
Buy Websites
Sell Your Website
Turnkey Websites
Trusted Escrow
New domains
News
Resources
note: the deliverable for this job is 4 tiles (not all of the above)as I want to get the design style sorted with you.

The website where these will appear sells pre-loved domains and turnkey websites. Also, some of these tiles will link through to a classifieds website which we will also want you to help create tiles for once this job is completed to satisfaction.

The files attached are samples only.

Target Market(s)

Domain buyers
Business owners
People buying websites

Industry/Entity Type

Advertising

Requirements
Must have
• Nice clean, clear text
Relevant
Nice to have
• Fun

```html
<!DOCTYPE html>
<html lang="en">
<head>
<meta charset="utf-8">
<title>Advertising Tiles</title>
<link rel="stylesheet" href="https://fonts.googleapis.com/css2?family=Marcellus&display=swap">
<style>
  :root {
    --page-bg: #ffffff;
    --tile-light: #cf4d4f;
    --tile-mid: #a3282b;
    --tile-dark: #6e0b0f;
    --chrome-edge: #2e2e2e;
  }
  html, body {
    margin: 0;
    padding: 0;
    width: 1200px;
    height: 1093px;
    overflow: hidden;
    background: var(--page-bg);
  }
  .tile-board {
    display: block;
    width: 1200px;
    height: 1093px;
  }
  .tile-bg { fill: url(#tileGlow); }
  .tile-label {
    font-family: "Marcellus", serif;
    fill: url(#chrome);
    stroke: var(--chrome-edge);
    stroke-width: 2.5px;
    paint-order: stroke fill;
    text-anchor: middle;
    filter: url(#labelShadow);
  }
  .label-large { font-size: 120px; }
  .label-small { font-size: 96px; }
  .stop-light { stop-color: var(--tile-light); }
  .stop-mid { stop-color: var(--tile-mid); }
  .stop-dark { stop-color: var(--tile-dark); }
</style>
</head>
<body>
<svg class="tile-board" viewBox="0 0 1200 1093" xmlns="http://www.w3.org/2000/svg">
  <defs>
    <radialGradient id="tileGlow" cx="50%" cy="50%" r="70%">
      <stop offset="0%" class="stop-light"/>
      <stop offset="55%" class="stop-mid"/>
      <stop offset="100%" class="stop-dark"/>
    </radialGradient>
    <linearGradient id="chrome" x1="0" y1="0" x2="0" y2="1">
      <stop offset="0%" stop-color="#ffffff"/>
      <stop offset="40%" stop-color="#e6e6e6"/>
      <stop offset="52%" stop-color="#8c8c8c"/>
      <stop offset="70%" stop-color="#f4f4f4"/>
      <stop offset="100%" stop-color="#9a9a9a"/>
    </linearGradient>
    <filter id="labelShadow" x="-10%" y="-20%" width="120%" height="140%">
      <feDropShadow dx="3" dy="4" stdDeviation="3" flood-color="#2a0000" flood-opacity="0.6"/>
    </filter>
  </defs>

  <g class="tile tile-domains">
    <rect class="tile-bg" x="0" y="0" width="587" height="533"/>
    <text class="tile-label label-large" x="293" y="235">Domains</text>
    <text class="tile-label label-large" x="293" y="373">For Sale</text>
  </g>

  <g class="tile tile-escrow">
    <rect class="tile-bg" x="613" y="0" width="587" height="533"/>
    <text class="tile-label label-large" x="906" y="227">Escrow</text>
    <text class="tile-label label-large" x="906" y="373">services</text>
  </g>

  <g class="tile tile-turnkey">
    <rect class="tile-bg" x="0" y="560" width="587" height="533"/>
    <text class="tile-label label-large" x="293" y="773">Turnkey</text>
    <text class="tile-label label-small" x="293" y="933">Websites</text>
  </g>

  <g class="tile tile-news">
    <rect class="tile-bg" x="613" y="560" width="587" height="533"/>
    <text class="tile-label label-large" x="888" y="880">News</text>
  </g>
</svg>
</body>
</html>
```